Office Warming Party. I attached an image (blogger flyer) that you can use as an example, or you can create one from scratch. I just want it to look clean but stylish like the example (but still professional). Text:

(ps if there is too much text, you can take out the last line and just put brantleylawgroup.com)

BRANTLEY LAW GROUP (logo attached with the skyline image, I will provide a better quality logo but this will work for the proof)

OFFICE WARMING PARTY
FRI NOV 15 2013 7-10PM
2742 K Avenue, Suite 410
Sacramento

Full Hosted Bar / Cocktail Attire

Music by SF's Marcus Tilden (larger text)
Also feat. Neil Ashby & Vance
Catering by Orvo, Saffrel, and Tosaki

Also a birthday party for Darnell Brantley. Invite only. Please RSVP
at www.eventgather.example/events/847203615924318

BRANTLEY LAW GROUP specializes in personal injury and criminal law, visit our site
at www.brantleylawgroup.com or call (916) 555-2817 for more information

It's not letting me attach the flyers so I'm including links to them:
http://www.gigpostline.example/images/uploads/flyers/blogger_holiday_party.jpg

http://www.valleyclaimhelp.example (brantley law group is top left)

Target Market(s)

Professionals but also house music lovers

Industry/Entity Type

Catering

Font styles to use
Sans Serif

Requirements
Must have
• Logo and DJ name bold or bigger (Marcus Tilden)

```html
<!DOCTYPE html>
<html lang="en">
<head>
<meta charset="utf-8">
<title>Brantley Law Group – Office Warming &amp; Birthday Party</title>
<link href="https://fonts.googleapis.com/css2?family=Oswald:wght@500;600&family=Dosis:wght@500;600;700&display=swap" rel="stylesheet">
<style>
  :root {
    --red: #c8141b;
    --ink: #2b2b2b;
    --grey: #7b7b7b;
    --light-grey: #a9a9a9;
    --rule: #c9c9c9;
    --paper-top: #ffffff;
    --paper-bottom: #e4e4e4;
    --band: #ffffff;
  }
  html, body { margin: 0; padding: 0; overflow: hidden; }
  body { width: 849px; height: 1200px; background: #ffffff; }
  .flyer {
    position: relative;
    width: 849px;
    height: 1200px;
    overflow: hidden;
    font-family: "Dosis", sans-serif;
    color: var(--ink);
  }
  .backdrop {
    position: absolute; inset: 0;
    background: radial-gradient(ellipse at 40% 35%, var(--paper-top) 0%, #f1f1f1 55%, var(--paper-bottom) 100%);
  }
  .brand {
    position: absolute; left: 87px; top: 48px;
    font-family: "Oswald", sans-serif; font-weight: 600;
    color: var(--red); font-size: 36px; line-height: 36px;
    letter-spacing: -0.5px; text-transform: uppercase;
  }
  .rule {
    position: absolute; left: 87px; width: 663px; height: 1px;
    background: var(--rule);
  }
  .title {
    position: absolute; font-family: "Oswald", sans-serif; font-weight: 600;
    color: var(--red); text-transform: uppercase; margin: 0; line-height: 1;
    letter-spacing: -1px;
  }
  .title-office { left: 84px; top: 156px; font-size: 110px; }
  .title-warming { left: 184px; top: 252px; font-size: 54px; }
  .title-party { right: 147px; top: 296px; font-size: 92px; }
  .line {
    position: absolute; left: 0; width: 849px; text-align: center;
    margin: 0; line-height: 1; white-space: nowrap;
  }
  .date {
    top: 392px; font-family: "Oswald", sans-serif; font-weight: 500;
    font-size: 60px; color: var(--grey); letter-spacing: -0.5px;
  }
  .venue { top: 454px; font-size: 38px; font-weight: 600; color: var(--grey); }
  .venue .city { margin-left: 22px; }
  .bar { top: 542px; font-size: 42px; font-weight: 700; color: var(--ink); }
  .music-by { top: 630px; font-size: 40px; font-weight: 700; color: var(--ink); }
  .headliner {
    top: 686px; font-family: "Oswald", sans-serif; font-weight: 600;
    font-size: 62px; color: var(--red); letter-spacing: -0.5px;
  }
  .support { top: 746px; font-size: 40px; font-weight: 700; color: var(--ink); }
  .support .lead { color: var(--light-grey); margin-right: 10px; }
  .catering { top: 830px; font-size: 32px; font-weight: 600; color: var(--grey); }
  .catering b { color: var(--ink); font-weight: 700; }
  .birthday { top: 902px; font-size: 31px; font-weight: 700; color: var(--grey); }
  .birthday .host { color: var(--red); }
  .birthday .lead { color: var(--ink); }
  .rsvp { top: 950px; font-size: 30px; font-weight: 700; color: var(--grey); }
  .rsvp .url { color: var(--ink); }
  .about { top: 1034px; font-size: 23px; font-weight: 700; color: var(--ink); }
  .contact { top: 1066px; font-size: 21px; font-weight: 700; color: var(--red); }
  .contact span { color: var(--grey); }
  .icon { display: inline-block; vertical-align: -4px; margin-right: 8px; }
  .footer-band {
    position: absolute; left: 0; top: 1118px; width: 849px; height: 54px;
    background: var(--band); box-shadow: 0 1px 4px rgba(0,0,0,0.12);
  }
  .footer-mark {
    position: absolute; right: 40px; top: 16px;
    font-family: "Oswald", sans-serif; font-weight: 500;
    font-size: 17px; color: var(--grey); text-transform: uppercase; letter-spacing: 0.5px;
  }
</style>
</head>
<body>
<main class="flyer">
  <div class="backdrop" role="img" aria-label="Soft grey background with large faint chain-link decoration"></div>

  <div class="brand">Brantley<br>Law Group</div>
  <div class="rule" style="top:162px"></div>

  <h1 class="title title-office">Office</h1>
  <div class="title title-warming">Warming &amp; Birthday</div>
  <div class="title title-party">Party</div>
  <div class="rule" style="top:387px"></div>

  <p class="line date">FRI NOV 15 2013 7-10PM</p>
  <p class="line venue">
    <svg class="icon" width="22" height="32" viewBox="0 0 22 32" aria-hidden="true"><path d="M11 1C5.5 1 1 5.3 1 10.8 1 18 11 31 11 31s10-13 10-20.2C21 5.3 16.5 1 11 1z" fill="#c8141b"/><circle cx="11" cy="10.5" r="3.6" fill="#fff"/></svg>2742 K Avenue, Suite 410<span class="city">Sacramento</span>
  </p>
  <div class="rule" style="top:510px"></div>

  <p class="line bar">Full Hosted Bar
    <svg class="icon" width="28" height="40" viewBox="0 0 28 40" aria-hidden="true" style="margin:0 4px 0 6px;vertical-align:-6px"><path d="M3 2h22c0 10-4 16-11 17C7 18 3 12 3 2z" fill="#c8141b"/><rect x="12.5" y="18" width="3" height="15" fill="#c8141b"/><rect x="6" y="33" width="16" height="3" rx="1" fill="#c8141b"/></svg>Cocktail Attire</p>
  <div class="rule" style="top:612px"></div>

  <p class="line music-by">
    <svg class="icon" width="46" height="30" viewBox="0 0 46 30" aria-hidden="true" style="margin-right:12px"><rect x="2" y="6" width="40" height="22" rx="3" fill="#c8141b" transform="rotate(-12 22 17)"/><circle cx="20" cy="17" r="7" fill="#fff"/><circle cx="20" cy="17" r="2" fill="#c8141b"/><rect x="32" y="6" width="3" height="13" fill="#fff" transform="rotate(-12 22 17)"/></svg>Music by</p>
  <p class="line headliner">SF’s Marcus Tilden</p>
  <p class="line support"><span class="lead">featuring</span>Neil Ashby &amp; Vance</p>
  <div class="rule" style="top:810px"></div>

  <p class="line catering">
    <svg class="icon" width="34" height="36" viewBox="0 0 34 36" aria-hidden="true"><rect x="2" y="2" width="2.5" height="12" fill="#c8141b"/><rect x="6.5" y="2" width="2.5" height="12" fill="#c8141b"/><rect x="11" y="2" width="2.5" height="12" fill="#c8141b"/><rect x="2" y="12" width="11.5" height="4" fill="#c8141b"/><rect x="6" y="15" width="4" height="20" rx="1.5" fill="#c8141b"/><ellipse cx="26" cy="9" rx="5" ry="8" fill="#c8141b"/><rect x="24" y="15" width="4" height="20" rx="1.5" fill="#c8141b"/></svg>Catering by <b>Orvo</b>, <b>Saffrel</b>, and <b>Tosaki</b></p>
  <div class="rule" style="top:882px"></div>

  <p class="line birthday">
    <svg class="icon" width="30" height="28" viewBox="0 0 30 28" aria-hidden="true"><rect x="3" y="13" width="24" height="13" rx="2" fill="#c8141b"/><rect x="1" y="24" width="28" height="3" fill="#c8141b"/><rect x="3" y="17" width="24" height="2" fill="#fff"/><rect x="8" y="5" width="2" height="7" fill="#c8141b"/><rect x="14" y="5" width="2" height="7" fill="#c8141b"/><rect x="20" y="5" width="2" height="7" fill="#c8141b"/></svg><span class="lead">A birthday party for</span> <span class="host">Darnell Brantley</span>. Invite only.</p>
  <p class="line rsvp">RSVP at <span class="url">www.eventgather.example/events/847203615924318</span></p>
  <div class="rule" style="top:1008px; left:87px; width:705px"></div>

  <p class="line about">BRANTLEY LAW GROUP specializes in personal injury and criminal law.</p>
  <p class="line contact">Visit <span>www.brantleylawgroup.com</span> or call <span>(916) 555-2817</span> for more information.</p>

  <footer class="footer-band">
    <div class="footer-mark">Brantley Law Group</div>
  </footer>
</main>
</body>
</html>
```